Specialized instructional design consultant needs a business card

**Hi Designers,
This project is put on hold until the logo project is completed. We will re-open this project at that time, if you are interested in the logo project see following link
http://jobs.pixelbazaar.example/job.aspx?id=472615

I need a business card that makes me stand out as an innovative, specialized professional that organizations can trust to lead their team through a project. I develop customized learning for the workflow - so my work is about being able to connect with my clients and their teams quickly and build their trust so we can develop the right solution. I like primary colours, designs that represent connections and movement. The final design should be clean, concise ... and cool.

Here are the details:

Company name is in the logo

Helen Marsh, B.A., M.Sc., CPTD
helen.marsh@quillpond.example

Ryan Marsh, CPA
ryan.marsh@quillpond.example

Location:
Victoria, British Columbia
Canada

Phone:
250.555.0184

Reason: I needed to delay the start of this project because my logo wasn't done. Now it is done so we can move forward.

Target Market(s)

Executives who have the authority to make decisions about whether or not to hire me as a consultant on their team

Industry/Entity Type

Business

Font styles to use
Sans Serif

Requirements
Must have
• Clean, concise, but stands out
keep it simple
depicts connections between individual parts
primary colours
Nice to have
• a sense of movement / flow

```html
<!DOCTYPE html>
<html lang="en">
<head>
<meta charset="utf-8">
<title>Quill Pond Consulting – Business Card Designs</title>
<link rel="stylesheet" href="https://fonts.googleapis.com/css2?family=Arimo:wght@400&display=swap">
<style>
  :root {
    --stage: #5e3528;
    --label: #ffffff;
    --card: #ffffff;
    --card-edge: #d8d8d8;
    --ink: #4a4a4a;
    --ink-soft: #5c5c5c;
    --brand: #6b6b6b;
    --accent: #e07a2c;
    --rule: #8a8a8a;
    --band: #555350;
    --band-text: #ffffff;
  }
  * { box-sizing: border-box; margin: 0; padding: 0; }
  html, body {
    width: 1200px; height: 900px; overflow: hidden;
    background: var(--stage);
    font-family: "Arimo", Arial, sans-serif;
  }
  .stage { position: relative; width: 1200px; height: 900px; }

  .design-label {
    position: absolute; top: 244px; width: 300px;
    text-align: center; color: var(--label);
    font-size: 40px; font-weight: 400; line-height: 48px;
  }
  .design-label--one { left: 224px; }
  .design-label--two { left: 682px; }

  .card {
    position: absolute; top: 334px; width: 400px; height: 230px;
    background: var(--card); border: 1px solid var(--card-edge);
    overflow: hidden;
  }
  .card--one { left: 172px; }
  .card--two { left: 628px; }

  .brand {
    position: absolute; display: flex; align-items: center; gap: 8px;
    color: var(--brand);
  }
  .card--one .brand { left: 38px; top: 104px; }
  .card--two .brand { left: 40px; top: 104px; }
  .brand__dot {
    width: 16px; height: 16px; border-radius: 50%;
    background: var(--accent); flex: none;
  }
  .brand__name { display: flex; flex-direction: column; line-height: 1; }
  .brand__title { font-size: 25px; letter-spacing: 0.3px; }
  .brand__sub { font-size: 15px; letter-spacing: 3.2px; margin-top: 6px; }

  .divider { position: absolute; width: 1px; background: var(--rule); }
  .card--one .divider { left: 220px; top: 60px; height: 114px; }
  .card--two .divider { left: 199px; top: 78px; height: 80px; }

  .contact { position: absolute; color: var(--ink); }
  .card--one .contact { left: 245px; top: 89px; }
  .card--two .contact { left: 239px; top: 90px; }
  .contact__name { font-size: 13.5px; line-height: 16px; }
  .contact__creds { font-size: 8.5px; color: var(--ink-soft); margin: 2px 0 0 1px; }
  .contact__phone { font-size: 9px; color: var(--ink-soft); margin: 9px 0 0 1px; }
  .contact__email { font-size: 9px; color: var(--ink-soft); margin: 2px 0 0 1px; }

  .location {
    position: absolute; left: 0; width: 100%; text-align: center;
    font-size: 11.5px;
  }
  .location--band {
    bottom: 0; height: 22px; line-height: 22px;
    background: var(--band); color: var(--band-text);
  }
  .location--plain { top: 198px; color: var(--ink); }
</style>
</head>
<body>
<main class="stage">
  <h2 class="design-label design-label--one">design 1</h2>
  <h2 class="design-label design-label--two">design 2</h2>

  <section class="card card--one">
    <div class="brand">
      <span class="brand__dot"></span>
      <span class="brand__name">
        <span class="brand__title">Quill Pond</span>
        <span class="brand__sub">consulting</span>
      </span>
    </div>
    <div class="divider"></div>
    <div class="contact">
      <p class="contact__name">Helen Marsh</p>
      <p class="contact__creds">B.A., M.Sc., CPTD</p>
      <p class="contact__phone">T : +1 250.555.0184</p>
      <p class="contact__email">helen.marsh@quillpond.example</p>
    </div>
    <p class="location location--band">Harrow Cove, Westland Province, Canada</p>
  </section>

  <section class="card card--two">
    <div class="brand">
      <span class="brand__dot"></span>
      <span class="brand__name">
        <span class="brand__title">Quill Pond</span>
        <span class="brand__sub">consulting</span>
      </span>
    </div>
    <div class="divider"></div>
    <div class="contact">
      <p class="contact__name">Ryan Marsh</p>
      <p class="contact__creds">CPA</p>
      <p class="contact__phone">T : +1 250.555.0184</p>
      <p class="contact__email">ryan.marsh@quillpond.example</p>
    </div>
    <p class="location location--plain">Harrow Cove, Westland Province, Canada</p>
  </section>
</main>
</body>
</html>
```